Powerpoint Template Background Design

We are looking to update our powerpoint background to align better with our recently updated logo. I've included our current logo (BankGothic Md BT Medium) and previous ppt background we had used for reference. Page orientation should be landscape. Should be usable online and as a printable deck. We are in the digital advertising sales industry and represent various digital ad products to ad agencies and clients who are interested in marketing their products using mobile advertising tools. the RGB color yellow in our logo is 245, 191,34 #fsbf22. We like to also see the grey and black in our logo included. We'd like it to be similar but new and refreshed from our previous ppt background. I've added our current sales deck for your review and consideration with your design.

Target Market(s)

Advertisers, Ad agencies

Industry/Entity Type

Advertising

Colors
ffc214

Requirements
Must have
• Include Logo. Preferably our 3d logo on the cover page. color scheme should match our logo. Must have cover page and template border page that we will use throughout the entire presentation.
Nice to have
• Full cover page graphic using our 3d logo and allows us to add text in a fixed area of the slide
Should not have
• If recommending full slide color/imagery please note it will be used both online and as a printable deck. Do not include the tagline and/or text from the previously used presentation template.

```html
<!DOCTYPE html>
<html lang="en">
<head>
<meta charset="utf-8">
<title>Northlight – Presentation Template Set</title>
<link href="https://fonts.googleapis.com/css2?family=Rajdhani:wght@400;500;600;700&display=swap" rel="stylesheet">
<style>
  :root {
    --canvas: #6b747c;
    --night-deep: #161b24;
    --night-mid: #3a4352;
    --gold: #f5bf22;
    --gold-soft: #fbe79a;
    --gold-pale: #fff6d8;
    --graphite: #5e6570;
    --ink: #2e2f33;
    --ink-soft: #55575c;
    --paper: #ffffff;
    --rule-light: rgba(255,255,255,0.55);
    --rule-dark: rgba(0,0,0,0.35);
  }
  * { margin: 0; padding: 0; box-sizing: border-box; }
  html, body {
    width: 1200px; height: 1000px; overflow: hidden;
    background: var(--canvas);
    font-family: "Rajdhani", "Arial Narrow", sans-serif;
  }
  .template-set { position: relative; width: 1200px; height: 1000px; }

  .slide {
    position: absolute; width: 564px; height: 396px; overflow: hidden;
    box-shadow: 0 2px 6px rgba(0,0,0,0.25);
  }
  .slide--cover-left  { left: 25px;  top: 92px; }
  .slide--cover-right { left: 613px; top: 92px; }
  .slide--doc-gold    { left: 25px;  top: 515px; }
  .slide--doc-white   { left: 613px; top: 515px; }

  .slide--dark {
    background: radial-gradient(ellipse 70% 80% at 55% 35%, var(--night-mid), var(--night-deep));
    color: var(--paper);
  }
  .slide--gold {
    background: radial-gradient(ellipse 60% 70% at 25% 25%, var(--gold-pale), var(--gold-soft) 45%, var(--gold) 100%);
    color: var(--ink);
  }
  .slide--white { background: var(--paper); color: var(--ink); }

  /* soft decorative field where the brand graphic sits */
  .key-graphic { position: absolute; }
  .slide--cover-left .key-graphic {
    left: 270px; top: 130px; width: 300px; height: 260px;
    background: radial-gradient(ellipse at 45% 55%, rgba(245,191,34,0.55), rgba(120,126,136,0.35) 45%, transparent 72%);
  }
  .slide--cover-right .key-graphic {
    left: 260px; top: -20px; width: 320px; height: 260px;
    background: radial-gradient(ellipse at 40% 50%, rgba(245,191,34,0.55), rgba(120,126,136,0.35) 45%, transparent 72%);
  }
  .slide--doc-gold .key-graphic {
    left: 90px; top: 0; width: 480px; height: 396px;
    background: radial-gradient(ellipse at 60% 45%, rgba(255,255,255,0.35), rgba(232,170,20,0.25) 50%, transparent 75%);
  }
  .slide--doc-white .key-graphic {
    left: 60px; top: 0; width: 504px; height: 396px;
    background: radial-gradient(ellipse at 55% 60%, rgba(245,191,34,0.14), rgba(150,150,150,0.14) 45%, transparent 72%);
  }

  .brand {
    position: absolute; display: flex; align-items: center; gap: 6px;
    font-weight: 600; font-size: 19px; letter-spacing: 2px; text-transform: uppercase;
  }
  .brand__dot { width: 9px; height: 9px; border-radius: 50%; background: var(--gold); }
  .slide--dark .brand { color: var(--paper); }
  .slide--gold .brand, .slide--white .brand { color: var(--ink); }
  .slide--cover-left .brand  { left: 400px; top: 82px; }
  .slide--cover-right .brand { left: 64px;  top: 86px; }
  .slide--doc-gold .brand    { left: 405px; top: 345px; }
  .slide--doc-white .brand   { left: 395px; top: 80px; }

  .title-block { position: absolute; }
  .title-block__title { font-weight: 600; font-size: 31px; line-height: 1; }
  .title-block__subtitle { font-weight: 500; font-size: 20px; line-height: 1.2; margin-top: 2px; }
  .slide--cover-left .title-block  { left: 65px; top: 90px; }
  .slide--cover-right .title-block { left: 65px; top: 166px; }
  .slide--doc-gold .title-block    { left: 71px; top: 109px; }
  .slide--doc-white .title-block   { left: 72px; top: 128px; }

  .meta { position: absolute; width: 215px; font-size: 11px; font-weight: 500; }
  .meta__date { padding-bottom: 4px; }
  .meta__presenter {
    display: grid; grid-template-columns: 76px 1fr; line-height: 15px;
    padding: 4px 0 5px;
  }
  .meta__url { margin-top: 14px; font-size: 9px; font-weight: 700; }
  .slide--dark .meta__date, .slide--dark .meta__presenter { border-bottom: 1px solid var(--rule-light); }
  .slide--gold .meta__date, .slide--gold .meta__presenter,
  .slide--white .meta__date, .slide--white .meta__presenter { border-bottom: 1px solid var(--rule-dark); }
  .slide--cover-right .meta__date, .slide--cover-right .meta__presenter { border-bottom: none; }
  .slide--cover-left .meta  { left: 62px; top: 270px; }
  .slide--cover-right .meta { left: 62px; top: 274px; }
  .slide--doc-gold .meta    { left: 68px; top: 259px; }
  .slide--doc-white .meta   { left: 69px; top: 276px; }
</style>
</head>
<body>
<main class="template-set">

  <section class="slide slide--dark slide--cover-left">
    <div class="key-graphic" role="img" aria-label="Brand graphic: gold and grey faceted star shape over a connected network of dots"></div>
    <div class="brand"><span class="brand__dot"></span>Northlight</div>
    <div class="title-block">
      <h1 class="title-block__title">Presentation Title</h1>
      <p class="title-block__subtitle">Subtitle of presentation</p>
    </div>
    <div class="meta">
      <p class="meta__date">12 March 2018</p>
      <div class="meta__presenter"><span>Presented by:</span><span>Daniel Marsh<br>Brand Development Manager</span></div>
      <p class="meta__url">www.northlightmedia.com</p>
    </div>
  </section>

  <section class="slide slide--dark slide--cover-right">
    <div class="key-graphic" role="img" aria-label="Brand graphic: gold and grey faceted star shape over a connected network of dots"></div>
    <div class="brand"><span class="brand__dot"></span>Northlight</div>
    <div class="title-block">
      <h1 class="title-block__title">Presentation Title</h1>
      <p class="title-block__subtitle">Subtitle of presentation</p>
    </div>
    <div class="meta">
      <p class="meta__date">12 March 2018</p>
      <div class="meta__presenter"><span>Presented by:</span><span>Daniel Marsh<br>Brand Development Manager</span></div>
      <p class="meta__url">www.northlightmedia.com</p>
    </div>
  </section>

  <section class="slide slide--gold slide--doc-gold">
    <div class="key-graphic" role="img" aria-label="Faint brand graphic: pale faceted star shape with a light dot network"></div>
    <div class="brand"><span class="brand__dot"></span>Northlight</div>
    <div class="title-block">
      <h1 class="title-block__title">Doc Presentation Title</h1>
      <p class="title-block__subtitle">Subtitle of presentation</p>
    </div>
    <div class="meta">
      <p class="meta__date">12 March 2018</p>
      <div class="meta__presenter"><span>Presented by:</span><span>Daniel Marsh<br>Brand Development Manager</span></div>
      <p class="meta__url">www.northlightmedia.com</p>
    </div>
  </section>

  <section class="slide slide--white slide--doc-white">
    <div class="key-graphic" role="img" aria-label="Faint brand graphic: pale gold and grey faceted star shape with a sweeping arc"></div>
    <div class="brand"><span class="brand__dot"></span>Northlight</div>
    <div class="title-block">
      <h1 class="title-block__title">Doc Presentation Title</h1>
      <p class="title-block__subtitle">Subtitle of presentation</p>
    </div>
    <div class="meta">
      <p class="meta__date">12 March 2018</p>
      <div class="meta__presenter"><span>Presented by:</span><span>Daniel Marsh<br>Brand Development Manager</span></div>
      <p class="meta__url">www.northlightmedia.com</p>
    </div>
  </section>

</main>
</body>
</html>
```